Zanquorra Business Card Design

Zanquorra is a small and new restaurant/ bar location in Hong Kong. The name "Djibouti" derives from an African country. There is no specific reason behind other than the fact, that the bar is somewhat inspired by African elements (only inspired but not purely based on African cuisine etc.).

The bar is somewhat a fusion of African, Mediterranean and Oriental (Old French Vietnam) elements.

However, it is very imperative to stress, that the overall look and feel of Zanquorra is a very high end cocktail lounge/ bar location. The bar is tucked away in a hidden alley, so people will have to know about it. The idea is to send the consumer off in an Escape or hidden remote location where they are at ease in a hip, stylish and trendy environment.

The card needs to feel high-end.

Final logo artwork has been attached and also pictures of the bar/ restaurant itself. The logo ie monkey head cannot be modified. However, the background color and the color of the type "ZANQUORRA" can be changed.

The following details need to fit onto the business card. Of course they can be arranged to your liking:

LOGO

Colin Vey
Partner

+852 97035164
xxx@zanquorra.com
www.zanquorra.com
7C, Brennick Road, Wan Chai, Hong Kong

```html
<!DOCTYPE html>
<html lang="en">
<head>
<meta charset="utf-8">
<title>Zanquorra Business Card</title>
<link href="https://fonts.googleapis.com/css2?family=Cinzel:wght@500&family=Open+Sans:wght@400;600&display=swap" rel="stylesheet">
<style>
  :root {
    --page-bg: #e4e4e4;
    --card-bg: #3a322d;
    --card-grain: #443b35;
    --ink-light: #f1eeea;
    --ink-muted: #cfc8c1;
    --rule: #6d625a;
  }
  * { margin: 0; padding: 0; box-sizing: border-box; }
  html, body {
    width: 1200px; height: 900px; overflow: hidden;
    background: radial-gradient(ellipse at center, #f2f2f2 0%, var(--page-bg) 70%, #cfcfcf 100%);
  }
  .canvas { position: relative; width: 1200px; height: 900px; }
  .card {
    position: absolute; width: 600px; height: 343px;
    background:
      radial-gradient(circle at 30% 20%, var(--card-grain) 0%, transparent 60%),
      var(--card-bg);
    box-shadow: 0 14px 30px rgba(0,0,0,0.35);
    color: var(--ink-light);
  }
  .card--back { left: 120px; top: 90px; }
  .card--front { left: 480px; top: 467px; }

  .contact {
    position: absolute; left: 48px; top: 60px; width: 250px;
    font-family: "Open Sans", sans-serif;
  }
  .contact__name { font-size: 22px; font-weight: 600; letter-spacing: 0.3px; }
  .contact__role { font-size: 17px; color: var(--ink-muted); margin-bottom: 16px; }
  .contact__address { font-size: 13px; line-height: 1.35; padding-left: 26px; margin-bottom: 4px; }
  .contact__line { display: flex; align-items: center; gap: 8px; font-size: 13px; line-height: 1.6; }
  .contact__line svg { width: 13px; height: 13px; flex: none; }

  .divider {
    position: absolute; left: 330px; top: 40px; bottom: 40px;
    width: 1px; background: var(--rule);
  }

  .brand {
    position: absolute; display: flex; flex-direction: column; align-items: center;
    font-family: "Cinzel", serif; font-weight: 500; color: var(--ink-light);
  }
  .brand__mark { border-radius: 50%; background: var(--ink-light); }
  .card--back .brand { left: 345px; top: 110px; width: 240px; }
  .card--back .brand__mark { width: 62px; height: 62px; margin-bottom: 12px; }
  .card--back .brand__name { font-size: 28px; letter-spacing: 2px; }
  .card--front .brand { left: 0; top: 70px; width: 600px; }
  .card--front .brand__mark { width: 120px; height: 120px; margin-bottom: 16px; }
  .card--front .brand__name { font-size: 54px; letter-spacing: 4px; }
</style>
</head>
<body>
<main class="canvas">
  <section class="card card--back" aria-label="Business card, contact side">
    <div class="contact">
      <p class="contact__name">Colin Vey</p>
      <p class="contact__role">Partner</p>
      <p class="contact__address">7C, Brennick Road, Wan Chai,<br>Hong Kong</p>
      <p class="contact__line">
        <svg viewBox="0 0 16 16" fill="currentColor"><path d="M3 1.5l2.5 0 1.2 3-1.6 1.2a9 9 0 0 0 5.2 5.2l1.2-1.6 3 1.2v2.5c0 .8-.7 1.5-1.5 1.5A12.5 12.5 0 0 1 1.5 3c0-.8.7-1.5 1.5-1.5z"/></svg>
        +852 97035164
      </p>
      <p class="contact__line">
        <svg viewBox="0 0 16 16" fill="none" stroke="currentColor" stroke-width="1.4"><rect x="1.5" y="3.5" width="13" height="9"/><path d="M1.5 3.5l6.5 5 6.5-5"/></svg>
        xxx@zanquorra.com
      </p>
      <p class="contact__line">
        <svg viewBox="0 0 16 16" fill="none" stroke="currentColor" stroke-width="1.3"><circle cx="8" cy="8" r="6.5"/><path d="M1.5 8h13M8 1.5c-3 3.5-3 9.5 0 13M8 1.5c3 3.5 3 9.5 0 13"/></svg>
        www.zanquorra.com
      </p>
    </div>
    <div class="divider"></div>
    <div class="brand">
      <div class="brand__mark"></div>
      <p class="brand__name">ZANQUORRA</p>
    </div>
  </section>

  <section class="card card--front" aria-label="Business card, brand side">
    <div class="brand">
      <div class="brand__mark"></div>
      <p class="brand__name">ZANQUORRA</p>
    </div>
  </section>
</main>
</body>
</html>
```